Real Estate Brokerage - Sales Promo Flyer

We would like someone to design a 8x11 high gloss promotional flyer for our real estate agents to use in the field when presenting to a possible listing client (someone who wants to sell their home).

The flyer should include some of our brokerage's recent sales transaction numbers, as well as benefits to using our service.

We would like our design to have a professional appeal, with bold colors, and vivid images.

I have attached 5 images of recently sold homes:
247 Marisol Lane Trust, Palm Beach Gardens, Florida - Sold for $424,000
4718 Tierra Linda Ct, Boca Raton, FL 33431 - Sold for $415,000
418 Verbena Hills Drive, Palm Beach Gardens, Florida - Sold for $877,500
20417 Heron Bluff Circle, West Palm Beach, Florida - Sold for $380,000
382 Thistle Road, Greenacres, Florida - Sold for $234,500

I can provide any additional details you need. See attached files.
Updates

This flyer should contain our business name, logo, phone numbers, and website (however you see fit). PelicoHomes Palm Beach County | (561) 402-1186 Broward County | (954) 238-4417 www.pelicohomes-example.com

More Properties to Add: 418 Verbena Hills Drive, Palm Beach Gardens, Florida - Sold for $877,500 20417 Heron Bluff Circle, West Palm Beach, Florida - Sold for $380,000 382 Thistle Road, Greenacres, Florida - Sold for $234,500

I have added the Original Logo Images. Please use one of these in your design.

I have uploaded an image of our syndication partners, please add this to your flyers.

Please submit all of your Design. Thanks!

Please submit your edits

Industry/Entity Type

Real Estate

Requirements
Must have
• PelicoHomes is one word with a capital K and capital R.

Must have website and phone number.

PelicoHomes
www.pelicohomes-example.com
561-402-1186 - Palm Beach County
954-238-4417 - Broward County

```html
<!DOCTYPE html>
<html lang="en">
<head>
<meta charset="utf-8">
<title>PelicoHomes – Recent Sales Flyer</title>
<link rel="stylesheet" href="https://fonts.googleapis.com/css2?family=Lato:ital,wght@0,300;0,400;0,700;1,400&family=Oswald:wght@400;500&display=swap">
<style>
  :root {
    --teal: #1fb3d2;
    --teal-deep: #1596b5;
    --paper: #ffffff;
    --paper-shade: #f0f0f0;
    --ink: #4a4a4a;
    --ink-soft: #6d6d6d;
    --rule: #b9b9b9;
    --footer: #7d7d7d;
    --photo-sky: #c9dcea;
    --photo-house: #d8c89a;
    --photo-garden: #5f8a45;
  }
  * { margin: 0; padding: 0; box-sizing: border-box; }
  html, body { width: 933px; height: 1200px; overflow: hidden; background: var(--paper); }
  .flyer {
    position: relative; width: 933px; height: 1200px; overflow: hidden;
    background: linear-gradient(180deg, var(--paper-shade) 0, var(--paper) 60%, var(--paper-shade) 100%);
    font-family: "Lato", sans-serif; color: var(--ink);
  }
  .brand-header {
    position: absolute; top: 0; left: 0; width: 100%; height: 114px;
    display: flex; align-items: center; justify-content: center; gap: 14px;
  }
  .brand-dot { width: 34px; height: 34px; border-radius: 50%; background: var(--teal); }
  .brand-name {
    font-family: "Lato", sans-serif; font-weight: 400; font-size: 30px;
    letter-spacing: 3px; color: var(--ink);
  }
  .hero { position: absolute; top: 114px; left: 0; width: 933px; height: 600px; }

  .sold-banner { position: absolute; left: 153px; top: 593px; width: 633px; height: 112px; display: flex; filter: drop-shadow(0 4px 5px rgba(0,0,0,.25)); }
  .sold-banner__address {
    width: 400px; background: var(--teal); color: #fff; padding: 20px 0 0 28px;
  }
  .sold-banner__street { font-weight: 700; font-size: 31px; line-height: 1.1; }
  .sold-banner__city { font-size: 21px; margin-top: 4px; }
  .sold-banner__price {
    flex: 1; background: var(--teal-deep); color: #fff; text-align: center; padding-top: 12px;
    clip-path: polygon(18px 0, 100% 0, 100% 82%, calc(100% - 18px) 100%, 0 100%, 0 0);
  }
  .sold-banner__label { font-size: 28px; font-weight: 700; }
  .sold-banner__amount { font-size: 43px; font-weight: 300; line-height: 1.1; }

  .section-title {
    position: absolute; top: 728px; left: 0; width: 100%;
    display: flex; align-items: center; justify-content: center; gap: 14px;
    font-style: italic; font-size: 25px; color: var(--ink-soft);
  }
  .section-title::before, .section-title::after { content: ""; width: 95px; height: 1px; background: var(--rule); }

  .recent-sales { position: absolute; top: 787px; left: 0; width: 100%; }
  .sale-card { position: absolute; width: 192px; text-align: center; }
  .sale-card__photo {
    width: 192px; height: 127px; border: 5px solid #fff;
    box-shadow: 0 3px 6px rgba(0,0,0,.3);
    background: linear-gradient(180deg, var(--photo-sky) 0, var(--photo-sky) 35%, var(--photo-house) 36%, var(--photo-house) 62%, var(--photo-garden) 63%);
  }
  .sale-card__street { font-family: "Oswald", sans-serif; font-size: 18px; color: var(--ink); margin-top: 14px; text-transform: uppercase; line-height: 1.1; white-space: nowrap; }
  .sale-card__city { font-size: 15px; color: var(--ink-soft); margin-top: 2px; }
  .sale-card__price { display: flex; align-items: center; justify-content: center; gap: 6px; margin-top: 8px; }
  .sale-card__pill { background: var(--teal); color: #fff; font-size: 11px; font-style: italic; padding: 3px 14px; }

  .contact-bar {
    position: absolute; left: 0; top: 1051px; width: 100%; height: 149px; background: var(--footer);
    display: flex; align-items: center; padding: 0 44px; color: #fff;
  }
  .contact-bar__call { font-family: "Oswald", sans-serif; font-weight: 500; font-size: 40px; letter-spacing: -0.5px; margin-right: 26px; }
  .contact-bar__lines { font-size: 19px; line-height: 1.5; }
  .contact-bar__badges { margin-left: auto; display: flex; gap: 36px; margin-right: 60px; }
  .badge { width: 48px; height: 48px; background: #3d3d3d; }
</style>
</head>
<body>
<main class="flyer">
  <header class="brand-header">
    <span class="brand-dot"></span>
    <span class="brand-name">PelicoHomes</span>
  </header>

  <svg class="hero" viewBox="0 114 933 600" aria-hidden="false">
    <defs>
      <linearGradient id="heroTone" x1="0" y1="0" x2="0" y2="1">
        <stop offset="0" stop-color="#cfe0ee"/>
        <stop offset="0.38" stop-color="#e3d3a4"/>
        <stop offset="0.72" stop-color="#cdb889"/>
        <stop offset="0.86" stop-color="#5d8a44"/>
        <stop offset="1" stop-color="#b58c6a"/>
      </linearGradient>
    </defs>
    <rect x="0" y="114" width="933" height="10" fill="var(--teal)"/>
    <path role="img" aria-label="Photo of the sold Mediterranean-style home with palm trees and tiled roof" d="M0 124 H933 V540 Q470 690 0 528 Z" fill="url(#heroTone)"/>
    <path d="M0 528 Q470 690 933 540" fill="none" stroke="var(--teal)" stroke-width="8"/>
  </svg>

  <section class="sold-banner">
    <div class="sold-banner__address">
      <div class="sold-banner__street">418 Verbena Hills Drive,</div>
      <div class="sold-banner__city">Palm Beach Gardens, Florida</div>
    </div>
    <div class="sold-banner__price">
      <div class="sold-banner__label">Sold for</div>
      <div class="sold-banner__amount">$877,500</div>
    </div>
  </section>

  <h2 class="section-title">Others Recent Sales</h2>

  <section class="recent-sales">
    <article class="sale-card" style="left:38px">
      <div class="sale-card__photo" role="img" aria-label="Photo of 247 Marisol Lane home"></div>
      <div class="sale-card__street">247 Marisol Lane Trust,</div>
      <div class="sale-card__city">Palm Beach Gardens, Florida</div>
      <div class="sale-card__price"><span class="sale-card__pill">Sold for $424,000</span>
        <svg width="14" height="12" viewBox="0 0 14 12"><path d="M1 6 L5 10 L13 1" fill="none" stroke="var(--teal)" stroke-width="2.2"/></svg></div>
    </article>
    <article class="sale-card" style="left:267px">
      <div class="sale-card__photo" role="img" aria-label="Photo of 20417 Heron Bluff Circle home"></div>
      <div class="sale-card__street">20417 Heron Bluff Circle</div>
      <div class="sale-card__city">West Palm Beach, Florida</div>
      <div class="sale-card__price"><span class="sale-card__pill">Sold for $380,000</span>
        <svg width="14" height="12" viewBox="0 0 14 12"><path d="M1 6 L5 10 L13 1" fill="none" stroke="var(--teal)" stroke-width="2.2"/></svg></div>
    </article>
    <article class="sale-card" style="left:487px">
      <div class="sale-card__photo" role="img" aria-label="Photo of 382 Thistle Road home"></div>
      <div class="sale-card__street">382 Thistle Road</div>
      <div class="sale-card__city">Greenacres, Florida</div>
      <div class="sale-card__price"><span class="sale-card__pill">Sold for $234,500</span>
        <svg width="14" height="12" viewBox="0 0 14 12"><path d="M1 6 L5 10 L13 1" fill="none" stroke="var(--teal)" stroke-width="2.2"/></svg></div>
    </article>
    <article class="sale-card" style="left:707px">
      <div class="sale-card__photo" role="img" aria-label="Photo of 4718 Tierra Linda Court home"></div>
      <div class="sale-card__street">4718 Tierra Linda Ct</div>
      <div class="sale-card__city">Boca Raton, Florida</div>
      <div class="sale-card__price"><span class="sale-card__pill">Sold for $415,000</span>
        <svg width="14" height="12" viewBox="0 0 14 12"><path d="M1 6 L5 10 L13 1" fill="none" stroke="var(--teal)" stroke-width="2.2"/></svg></div>
    </article>
  </section>

  <footer class="contact-bar">
    <div class="contact-bar__call">CALL US NOW:</div>
    <div class="contact-bar__lines">
      <div>(561) 402-1186 | Palm Beach County</div>
      <div>(954) 238-4417 | Broward County</div>
      <div>www.pelicohomes-example.com</div>
    </div>
    <div class="contact-bar__badges">
      <span class="badge" role="img" aria-label="Association membership badge"></span>
      <span class="badge" role="img" aria-label="Housing opportunity badge"></span>
    </div>
  </footer>
</main>
</body>
</html>
```